New Business Cards for NYC Salon

We are updating all of our cards. 7142-2869-4057 is my account number. We put names of our stylists on their cards. The back should include appointment space. Were looking for something more sleek and modern. Black/White Silver... or even touches of the orange color on our website which has been our thing for years. The design should communicate professional upscale boutique salon for men and women. Should be able to incorporate design into thank you cards, referral cards, brochure and postcards. The file is a zip file...we like the stacked ones black or white or the side versions.

Industry/Entity Type

Beauty Salon

Contact Information for Business Card

Marcus John's Salon313 W. 53rd Street, New York NY 10019 212-386-7714 info@marcusdellsalon.example www.marcusdellsalon.example

Font styles to use
Other font styles liked:
• trajan

Requirements
Must have
• we print a different card for every person in the salon. Begin by designing with the name Marcus. We will change it with every employee when printing. Must have a space for appointment date and time.
Nice to have
• Were looking to move towards the stacked or side placed logo but not opposed to utilizing the circular.
Should not have
• Photos

```html
<!DOCTYPE html>
<html lang="en">
<head>
<meta charset="utf-8">
<title>Marcus Dell's Salon – Business Card</title>
<link rel="stylesheet" href="https://fonts.googleapis.com/css2?family=Cinzel:wght@400;500&display=swap">
<style>
  :root {
    --ink: #111111;
    --black: #070707;
    --paper: #ffffff;
    --silver: #bcbec0;
    --orange: #f7941d;
    --dots: #8a8a8a;
    --stage-center: #a7a7a7;
    --stage-edge: #050505;
  }
  * { margin: 0; padding: 0; box-sizing: border-box; }
  html, body { width: 1200px; height: 800px; overflow: hidden; }
  body {
    position: relative;
    font-family: "Cinzel", "Trajan Pro", serif;
    color: var(--ink);
    background: radial-gradient(ellipse 55% 60% at 50% 50%, var(--stage-center) 0%, #4a4a4a 55%, var(--stage-edge) 100%);
  }
  .card { position: absolute; left: 306px; width: 590px; height: 345px; background: var(--paper); overflow: hidden; }
  .card-front { top: 45px; }
  .card-back { top: 408px; }

  /* front: brand area */
  .brand { position: absolute; left: 0; top: 0; width: 368px; height: 218px; text-align: center; }
  .brand-dot { position: absolute; left: 180px; top: 62px; width: 12px; height: 12px; border-radius: 50%; background: var(--ink); }
  .brand-name { position: absolute; left: 0; right: 0; top: 154px; font-size: 17px; letter-spacing: 4px; line-height: 1; }
  .brand-sub { position: absolute; left: 0; right: 0; top: 178px; font-size: 12px; letter-spacing: 3px; line-height: 1; }

  /* front: stylists panel */
  .stylists { position: absolute; left: 368px; top: 0; width: 222px; height: 218px; background: var(--silver); }
  .stylists-label { position: absolute; left: 26px; top: 28px; font-size: 9px; letter-spacing: 1px; }
  .stylists-art { position: absolute; left: 24px; top: 44px; width: 54px; height: 56px; border-radius: 50% 46% 48% 52%; background: linear-gradient(135deg, #1a1a1a, #3a3a3a); }
  .stylist-list { position: absolute; left: 90px; top: 28px; list-style: none; }
  .stylist { display: flex; align-items: center; height: 27px; font-size: 11px; letter-spacing: 1.6px; }
  .stylist svg { width: 11px; height: 10px; margin-right: 10px; }

  /* front: contact band */
  .contact { position: absolute; left: 0; top: 218px; width: 590px; height: 127px; background: var(--black); color: var(--paper); }
  .contact-item { position: absolute; font-size: 10px; letter-spacing: 1px; line-height: 1; }
  .contact-icon { position: absolute; width: 16px; height: 16px; }
  .divider { position: absolute; left: 296px; top: 18px; width: 2px; height: 71px; background: var(--orange); }
  .phone { font-size: 13px; letter-spacing: 1.2px; }

  /* back */
  .appt-kicker { position: absolute; left: 30px; top: 34px; font-size: 10px; letter-spacing: 1px; }
  .appt-title { position: absolute; left: 30px; top: 47px; font-size: 20px; letter-spacing: 1.5px; font-weight: 400; }
  .back-brand { position: absolute; left: 408px; top: 40px; display: flex; align-items: center; }
  .back-brand-dot { width: 8px; height: 8px; border-radius: 50%; background: var(--ink); margin-right: 12px; }
  .back-brand-text { text-align: center; line-height: 1; }
  .back-brand-name { font-size: 10px; letter-spacing: 2.2px; }
  .back-brand-sub { font-size: 7px; letter-spacing: 1.6px; margin-top: 3px; }
  .field { position: absolute; left: 30px; right: 30px; display: flex; align-items: flex-end; font-size: 11px; letter-spacing: 0.8px; line-height: 1; }
  .field-line { flex: 1; border-bottom: 1px dotted var(--dots); margin-left: 4px; height: 9px; }
</style>
</head>
<body>

<section class="card card-front">
  <div class="brand">
    <span class="brand-dot"></span>
    <div class="brand-name">Marcus Dell's</div>
    <div class="brand-sub">Salon</div>
  </div>

  <aside class="stylists">
    <div class="stylists-label">Stylists</div>
    <div class="stylists-art" role="img" aria-label="Dark silhouette illustration of two stylist heads with scissors"></div>
    <ul class="stylist-list">
      <li class="stylist"><svg viewBox="0 0 11 10"><path d="M1 9 Q2 4 7 3" fill="none" stroke="#f7941d" stroke-width="1.6"/><path d="M6 0 L11 3 L6 6 Z" fill="#f7941d"/></svg>Marcus</li>
      <li class="stylist"><svg viewBox="0 0 11 10"><path d="M1 9 Q2 4 7 3" fill="none" stroke="#f7941d" stroke-width="1.6"/><path d="M6 0 L11 3 L6 6 Z" fill="#f7941d"/></svg>Brianna</li>
      <li class="stylist"><svg viewBox="0 0 11 10"><path d="M1 9 Q2 4 7 3" fill="none" stroke="#f7941d" stroke-width="1.6"/><path d="M6 0 L11 3 L6 6 Z" fill="#f7941d"/></svg>Joy</li>
      <li class="stylist"><svg viewBox="0 0 11 10"><path d="M1 9 Q2 4 7 3" fill="none" stroke="#f7941d" stroke-width="1.6"/><path d="M6 0 L11 3 L6 6 Z" fill="#f7941d"/></svg>Annabel</li>
      <li class="stylist"><svg viewBox="0 0 11 10"><path d="M1 9 Q2 4 7 3" fill="none" stroke="#f7941d" stroke-width="1.6"/><path d="M6 0 L11 3 L6 6 Z" fill="#f7941d"/></svg>Lorenzo</li>
      <li class="stylist"><svg viewBox="0 0 11 10"><path d="M1 9 Q2 4 7 3" fill="none" stroke="#f7941d" stroke-width="1.6"/><path d="M6 0 L11 3 L6 6 Z" fill="#f7941d"/></svg>Nadia</li>
    </ul>
  </aside>

  <footer class="contact">
    <svg class="contact-icon" style="left:45px;top:17px" viewBox="0 0 16 16"><path d="M8 0a5.5 5.5 0 0 0-5.5 5.5C2.5 10 8 16 8 16s5.5-6 5.5-10.5A5.5 5.5 0 0 0 8 0z" fill="#f7941d"/><circle cx="8" cy="5.5" r="2" fill="#070707"/></svg>
    <div class="contact-item" style="left:73px;top:19px">Marcus Dell's Salon</div>
    <div class="contact-item" style="left:73px;top:45px">748 E. 29th Street,</div>
    <div class="contact-item" style="left:73px;top:64px">New York NY 10016</div>

    <div class="divider"></div>

    <svg class="contact-icon" style="left:323px;top:15px" viewBox="0 0 16 16"><rect x="1" y="3" width="14" height="10" fill="#f7941d"/><path d="M1 3 L8 9 L15 3" fill="none" stroke="#070707" stroke-width="1.2"/></svg>
    <div class="contact-item" style="left:351px;top:18px">info@marcusdellsalon.example</div>

    <svg class="contact-icon" style="left:323px;top:42px" viewBox="0 0 16 16"><circle cx="8" cy="8" r="7.5" fill="#f7941d"/><g fill="none" stroke="#070707" stroke-width="1"><ellipse cx="8" cy="8" rx="3" ry="7"/><line x1="1" y1="8" x2="15" y2="8"/><line x1="2" y1="4.5" x2="14" y2="4.5"/><line x1="2" y1="11.5" x2="14" y2="11.5"/></g></svg>
    <div class="contact-item" style="left:351px;top:45px">www.marcusdellsalon.example</div>

    <svg class="contact-icon" style="left:323px;top:71px" viewBox="0 0 16 16"><circle cx="8" cy="8" r="8" fill="#f7941d"/><path d="M5 4 L6.6 4 L7.4 6 L6.4 7 Q7.3 8.8 9 9.6 L10 8.6 L12 9.4 L12 11 Q11.5 12 10.5 12 Q5.5 11.5 4 5.5 Q4 4.5 5 4 Z" fill="#070707"/></svg>
    <div class="contact-item phone" style="left:351px;top:73px">212-386-7714</div>
  </footer>
</section>

<section class="card card-back">
  <div class="appt-kicker">Your next</div>
  <h2 class="appt-title">Appointment</h2>

  <div class="back-brand">
    <span class="back-brand-dot"></span>
    <div class="back-brand-text">
      <div class="back-brand-name">Marcus Dell's</div>
      <div class="back-brand-sub">Salon</div>
    </div>
  </div>

  <div class="field" style="top:124px"><span>Name:</span><span class="field-line"></span></div>
  <div class="field" style="top:160px"><span>Date:</span><span class="field-line"></span></div>
  <div class="field" style="top:195px"><span>Notes:</span><span class="field-line"></span></div>
  <div class="field" style="top:229px"><span class="field-line" style="margin-left:0"></span></div>
  <div class="field" style="top:265px"><span class="field-line" style="margin-left:0"></span></div>
  <div class="field" style="top:301px"><span class="field-line" style="margin-left:0"></span></div>
</section>

</body>
</html>
```